Large sticker for Oil Tanker

We need a sticker design for the rear of an oil tanker used to deliver heating oil in UK.

The idea of the sicker is to promote the fact that the tanker is delivering to a "buying group" who's orders have been grouped together to lower costs.

Central to the theme will be a picture of the founder of the buying group (Me..Clive Harrowby) but flanked on either side by a few of my members.

The idea would be to imitate the attached image

I would like the style to be close to the image I have uploaded and use photoshop to airbrush in faces for me and a few of my members.

```html
<!DOCTYPE html>
<html lang="en">
<head>
<meta charset="utf-8">
<title>Kindred Fuel Club – Tanker Sticker</title>
<link rel="stylesheet" href="https://fonts.googleapis.com/css2?family=Cinzel:wght@400;600;700&family=Marcellus&display=swap">
<style>
  :root {
    --bg-centre: #fffaf6;
    --bg-edge: #fbd6bb;
    --ink: #6a5150;
    --ink-dark: #5c4444;
    --band: #c5b7b7;
    --accent: #f6a46c;
    --halo: rgba(255, 255, 255, 0.95);
    --skin: #e2b89c;
    --skin-light: #f0d2bd;
    --skin-shade: #c4917a;
    --hair-blonde: #efdcae;
    --hair-brown: #6e4c3a;
    --cloth-dark: #6f6b72;
    --cloth-light: #d8c6b4;
    --pixel-grey: #b09486;
  }
  html, body { margin: 0; padding: 0; overflow: hidden; }
  .sticker {
    position: relative;
    width: 1200px;
    height: 646px;
    overflow: hidden;
    background: radial-gradient(ellipse 75% 70% at 50% 48%, var(--bg-centre) 0%, #fdeee2 55%, var(--bg-edge) 100%);
    font-family: "Cinzel", serif;
  }
  .headline {
    position: absolute;
    top: 88px; left: 0; width: 100%;
    margin: 0;
    text-align: center;
    font-weight: 600;
    font-size: 43px;
    letter-spacing: 1px;
    color: var(--ink);
  }
  .member {
    position: absolute;
    display: flex;
    flex-direction: column;
    align-items: center;
    transform: translateX(-50%);
  }
  .portrait {
    border-radius: 46% 46% 40% 40% / 44% 44% 36% 36%;
    box-shadow: 0 0 5px 5px var(--halo), inset 0 0 10px 4px rgba(255, 255, 255, 0.55);
  }
  .tone-bald {
    background: linear-gradient(180deg, var(--skin-light) 0%, var(--skin) 35%, var(--skin-shade) 68%, var(--cloth-dark) 100%);
  }
  .tone-blonde {
    background: linear-gradient(180deg, var(--hair-blonde) 0%, #f2dcc0 30%, #eab9a2 62%, var(--cloth-light) 100%);
  }
  .tone-brunette {
    background: linear-gradient(180deg, var(--hair-brown) 0%, #84604a 28%, #d9ac92 55%, #a58a7a 100%);
  }
  .tone-grey {
    background: linear-gradient(180deg, #cbb0a2 0%, var(--pixel-grey) 40%, #c2a08e 70%, #9a8c84 100%);
  }
  .tone-founder {
    background: linear-gradient(180deg, var(--skin-light) 0%, #e6c2a8 30%, #cfa088 55%, #7d5e4e 78%, var(--cloth-dark) 100%);
  }
  .member-name {
    margin-top: 5px;
    font-family: "Marcellus", serif;
    color: var(--ink);
    white-space: nowrap;
  }
  .founder .member-name { font-size: 13px; }
  .name-band {
    position: absolute;
    left: 148px; top: 366px;
    width: 910px; height: 110px;
    border-radius: 16px;
    background: var(--band);
    box-shadow: 0 3px 8px rgba(90, 60, 50, 0.35);
    display: flex;
    align-items: center;
    justify-content: center;
  }
  .brand-name {
    margin: 0;
    font-family: "Cinzel", serif;
    font-weight: 400;
    font-size: 76px;
    color: var(--ink-dark);
    letter-spacing: 1px;
  }
  .web-address {
    position: absolute;
    top: 498px; left: 0; width: 100%;
    margin: 0;
    text-align: center;
    font-weight: 700;
    font-size: 48px;
    letter-spacing: 2px;
    color: var(--accent);
    text-shadow: 2px 2px 3px rgba(110, 80, 70, 0.55);
  }
</style>
</head>
<body>
<main class="sticker">
  <h2 class="headline">SOME TEXT HERE</h2>

  <section class="members">
    <div class="member" style="left:208px; top:236px;">
      <div class="portrait tone-bald" style="width:52px; height:72px;" role="img" aria-label="Photo of a member"></div>
      <span class="member-name" style="font-size:7px;">Barney Lodge</span>
    </div>
    <div class="member" style="left:268px; top:220px;">
      <div class="portrait tone-blonde" style="width:64px; height:88px;" role="img" aria-label="Photo of a member"></div>
      <span class="member-name" style="font-size:8px;">Barney Lodge</span>
    </div>
    <div class="member" style="left:338px; top:212px;">
      <div class="portrait tone-brunette" style="width:66px; height:96px;" role="img" aria-label="Photo of a member"></div>
      <span class="member-name" style="font-size:8px;">Barney Lodge</span>
    </div>
    <div class="member" style="left:412px; top:208px;">
      <div class="portrait tone-grey" style="width:68px; height:100px;" role="img" aria-label="Photo of a member"></div>
      <span class="member-name" style="font-size:9px;">Barney Lodge</span>
    </div>
    <div class="member" style="left:500px; top:190px;">
      <div class="portrait tone-bald" style="width:92px; height:126px;" role="img" aria-label="Photo of a member"></div>
      <span class="member-name" style="font-size:10px;">Barney Lodge</span>
    </div>
    <div class="member founder" style="left:600px; top:146px;">
      <div class="portrait tone-founder" style="width:112px; height:168px;" role="img" aria-label="Photo of the founder, Clive Harrowby"></div>
      <span class="member-name">Clive Harrowby</span>
    </div>
    <div class="member" style="left:703px; top:180px;">
      <div class="portrait tone-blonde" style="width:88px; height:132px;" role="img" aria-label="Photo of a member"></div>
      <span class="member-name" style="font-size:10px;">Barney Lodge</span>
    </div>
    <div class="member" style="left:790px; top:198px;">
      <div class="portrait tone-brunette" style="width:72px; height:110px;" role="img" aria-label="Photo of a member"></div>
      <span class="member-name" style="font-size:9px;">Barney Lodge</span>
    </div>
    <div class="member" style="left:860px; top:220px;">
      <div class="portrait tone-bald" style="width:62px; height:92px;" role="img" aria-label="Photo of a member"></div>
      <span class="member-name" style="font-size:8px;">Barney Lodge</span>
    </div>
    <div class="member" style="left:930px; top:226px;">
      <div class="portrait tone-grey" style="width:60px; height:88px;" role="img" aria-label="Photo of a member"></div>
      <span class="member-name" style="font-size:8px;">Barney Lodge</span>
    </div>
    <div class="member" style="left:994px; top:234px;">
      <div class="portrait tone-blonde" style="width:52px; height:76px;" role="img" aria-label="Photo of a member"></div>
      <span class="member-name" style="font-size:7px;">Barney Lodge</span>
    </div>
  </section>

  <div class="name-band">
    <h1 class="brand-name">Kindred Fuel Club</h1>
  </div>

  <p class="web-address">WWW.KINDRED-FUEL.NET</p>
</main>
</body>
</html>
```